Business card and logo designs

We are looking to create a cool and trendy image for the company, some thing what quince has. We already have a logo, but we can reconsider a new logo.

Vorilo provides a new kind of web service for businesses to take appointments using web and mobile. Usually a customer needs to call or check several times. Vorilo solves this trouble. Our service refills cancellations quickly and automatically plus reduces no-shows. On top of that, our analytical tools give deep business and customer insights to increase revenue.

Phone bookings and cancellations are frustrating, time-consuming and expensive.It can take hours to book a 20 min appointment for e.g. with your doctor. When customers don’t find a suitable time, they need to call or check online again and again. Vorilo turn the tables and enables your doctor to get back to you with appointment of your choice,automatically. It refills cancellations quickly and automatically. Vrolio did not invent a booking system, like Quince did not invest a mobile phone. However, we make it mobile, intelligent and useful.

Vorilo identity should present a change, the same one which quince brought to mobile. Despite the fact that booking systems has been around for 2 decades, we change the game.

We want to communicate that we are saving time for consumers and businesses in an an innovative way and helping businesses to improve revenue.

Reason: We want more design entries.

Contents of the business card....

But we want the empty template so when new people join, we use the same.

Bram Tolvek

+358-402739158

Founder & CEO 

bram.tolvek@vorilo-example.net

 Vorilo Solutions Oy

Helsinki, Finland

www.vorilo-example.net

All,

We have to get ideas about a new logo. New business card is not enough.

Reason: More designs needed...

Reason: We have got very few good designs so far.

Reason: Need a bite more time... our creative director was busy

Target Market(s)

Most developed countries

Industry/Entity Type

Doctor

Requirements
Must have
• Color orange and green....
Should not have
• Should not have the obvious things... more intelligent design...

```html
<!DOCTYPE html>
<html lang="en">
<head>
<meta charset="utf-8">
<title>Vorilo stationery</title>
<link rel="stylesheet" href="https://fonts.googleapis.com/css2?family=Barlow:wght@400;600&display=swap">
<style>
  :root {
    --backdrop: #2a2a2a;
    --paper: #ffffff;
    --paper-shade: #f1f1f1;
    --ink: #2b2b2b;
    --ink-soft: #3a3a3a;
    --orange: #fbab3a;
    --orange-deep: #f5821f;
    --green: #6fb33f;
    --charcoal: #2d2d2d;
    --charcoal-light: #3b3b3b;
    --faint: #5a5a5a;
  }
  * { margin: 0; padding: 0; box-sizing: border-box; }
  html, body { width: 1200px; height: 900px; overflow: hidden; }
  body {
    background: var(--backdrop);
    font-family: "Barlow", Arial, sans-serif;
    position: relative;
  }
  .wordmark {
    font-weight: 600;
    letter-spacing: -0.5px;
    line-height: 1;
    white-space: nowrap;
  }
  .tab { position: absolute; left: 0; }

  /* letterhead */
  .letterhead {
    position: absolute; left: 436px; top: 109px;
    width: 697px; height: 800px;
    background: linear-gradient(90deg, var(--paper-shade), var(--paper) 40%);
    border-top-right-radius: 14px;
  }
  .letterhead .tab { top: 36px; }
  .letterhead .wordmark {
    position: absolute; left: 76px; top: 66px;
    font-size: 32px; color: var(--ink);
  }
  .letterhead .sender {
    position: absolute; right: 22px; top: 57px;
    text-align: right; font-size: 11px; line-height: 13px; color: var(--ink-soft);
    font-style: normal; white-space: nowrap;
  }
  .letterhead .web { margin-top: 13px; color: var(--green); }
  .letterhead .rule {
    position: absolute; left: 0; right: 0; top: 155px;
    height: 1px; background: var(--orange);
  }

  /* business card, front */
  .card { position: absolute; width: 300px; height: 183px; }
  .card-front {
    left: 195px; top: 251px; background: var(--paper);
    border-radius: 0 12px 12px 0;
  }
  .card-front .tab { top: 21px; }
  .card-front .wordmark {
    position: absolute; left: 30px; top: 86px; font-size: 25px; color: var(--ink);
  }
  .card-front .details {
    position: absolute; left: 130px; top: 42px;
    font-size: 10px; line-height: 12.5px; color: var(--ink-soft);
    white-space: nowrap;
  }
  .card-front .name { font-size: 15px; line-height: 17px; color: var(--ink); }
  .card-front .company { margin-top: 13px; }
  .card-front .web { margin-top: 13px; color: var(--green); }

  /* business card, orange back */
  .card-back-orange {
    left: 197px; top: 446px;
    background: linear-gradient(160deg, var(--orange) 55%, var(--orange-deep));
    border-radius: 0 12px 0 12px;
  }
  .card-back-orange .line {
    position: absolute; left: 0; right: 0; top: 56px; height: 1px; background: rgba(255,255,255,0.25);
  }
  .card-back-orange .tab { top: 70px; }
  .card-back-orange .wordmark {
    position: absolute; left: 0; right: 0; top: 74px; text-align: center;
    font-size: 34px; color: var(--paper);
  }

  /* business card, dark back */
  .card-back-dark {
    left: 464px; top: 573px;
    background: linear-gradient(160deg, var(--charcoal) 55%, var(--charcoal-light));
    border-radius: 0 12px 0 12px;
  }
  .card-back-dark .tab { top: 36px; }
  .card-back-dark .wordmark {
    position: absolute; left: 0; right: 0; top: 74px; text-align: center;
    font-size: 34px; color: var(--paper);
  }
  .card-back-dark .line {
    position: absolute; left: 0; right: 0; top: 136px; height: 1px; background: var(--green);
    opacity: 0.7;
  }

  /* faint mark on backdrop */
  .backdrop-mark { position: absolute; left: 0; top: 792px; }
  .backdrop-mark .bar { position: absolute; left: 0; top: 4px; width: 26px; height: 56px; background: var(--faint); }
  .backdrop-mark .wordmark {
    position: absolute; left: 90px; top: 0; font-size: 64px; color: var(--faint);
  }
</style>
</head>
<body>

  <section class="letterhead">
    <svg class="tab" width="24" height="58" viewBox="0 0 24 58" aria-hidden="true">
      <polygon points="0,0 24,0 24,46 0,58" fill="#fbab3a"/>
    </svg>
    <div class="wordmark">Vorilo</div>
    <address class="sender">
      <div>Vorilo Solutions Oy</div>
      <div>Helsinki, Finland</div>
      <div>+358-402739158</div>
      <div class="web">www.vorilo-example.net</div>
    </address>
    <div class="rule"></div>
  </section>

  <section class="card card-front">
    <svg class="tab" width="16" height="40" viewBox="0 0 16 40" aria-hidden="true">
      <polygon points="0,0 16,0 16,30 0,40" fill="#fbab3a"/>
    </svg>
    <div class="wordmark">Vorilo</div>
    <div class="details">
      <div class="name">Bram Tolvek</div>
      <div>Founder &amp; CEO</div>
      <div class="company">Vorilo Solutions Oy</div>
      <div>Helsinki, Finland</div>
      <div>+358-402739158</div>
      <div>bram.tolvek@vorilo-example.net</div>
      <div class="web">www.vorilo-example.net</div>
    </div>
  </section>

  <section class="card card-back-orange">
    <div class="line"></div>
    <svg class="tab" width="16" height="36" viewBox="0 0 16 36" aria-hidden="true">
      <polygon points="0,0 16,0 16,26 0,36" fill="#f5821f"/>
    </svg>
    <div class="wordmark">Vorilo</div>
  </section>

  <section class="card card-back-dark">
    <svg class="tab" width="16" height="40" viewBox="0 0 16 40" aria-hidden="true">
      <polygon points="0,0 16,0 16,30 0,40" fill="#6fb33f"/>
    </svg>
    <div class="wordmark">Vorilo</div>
    <div class="line"></div>
  </section>

  <div class="backdrop-mark">
    <div class="bar"></div>
    <div class="wordmark">Vorilo</div>
  </div>

</body>
</html>
```